letter head for a construction company

Company Name: Kaleshi Construction Limited

Address: Tumbili Street, Kigamboni Shores, Dar es salaam, Tanzania

Phone: 0754382916

email : info@kaleshiconstruction.example

website : www.kaleshiconstruction.example

```html
<!DOCTYPE html>
<html lang="en">
<head>
<meta charset="utf-8">
<title>Kaleshi Construction Limited – Letterhead</title>
<link href="https://fonts.googleapis.com/css2?family=Lato:wght@300;400;700;900&family=Allura&display=swap" rel="stylesheet">
<style>
  :root {
    --orange: #e77b27;
    --orange-soft: #ec9150;
    --charcoal: #454545;
    --ink: #2f2f2f;
    --backdrop: #e3e3e3;
    --paper: #ffffff;
    --paper-edge: #f1f0f0;
  }
  * { margin: 0; padding: 0; box-sizing: border-box; }
  html, body { width: 1153px; height: 1200px; overflow: hidden; }
  body {
    background: var(--backdrop);
    font-family: "Lato", Arial, sans-serif;
    color: var(--ink);
  }
  .letterhead {
    position: absolute;
    left: 148px; top: 0;
    width: 857px; height: 1200px;
    background: radial-gradient(ellipse at 50% 40%, var(--paper) 20%, var(--paper-edge) 85%);
    overflow: hidden;
  }

  /* Brand block */
  .brand { position: absolute; left: 64px; top: 66px; color: var(--charcoal); }
  .brand-name { font-weight: 900; font-size: 57px; line-height: 50px; letter-spacing: 2px; }
  .brand-sub { font-weight: 400; font-size: 20px; line-height: 20px; letter-spacing: 7.6px; margin-top: 4px; }

  /* Contact block */
  .contact {
    position: absolute;
    left: 536px; top: 55px;
    height: 114px;
    border-left: 1.5px solid var(--orange);
    padding-left: 12px;
    font-style: normal;
    font-size: 15px;
    color: #222;
  }
  .contact-title { font-weight: 900; font-size: 14px; line-height: 16px; color: var(--charcoal); }
  .contact-title .accent { color: var(--orange); }
  .contact-address { line-height: 19px; margin-top: 1px; }
  .contact-list { list-style: none; margin-top: 6px; }
  .contact-list li { display: flex; align-items: center; height: 20px; }
  .contact-list svg { width: 14px; height: 14px; margin-right: 12px; flex: none; }

  /* Letter body */
  .letter { position: absolute; left: 66px; width: 725px; font-size: 16.2px; line-height: 19.5px; }
  .date { top: 265px; }
  .recipient { top: 305px; }
  .company { top: 362px; }
  .salutation { top: 444px; font-weight: 700; font-size: 21px; line-height: 26px; color: var(--charcoal); }
  .body-text { text-align: justify; line-height: 18.5px; }
  .para-1 { top: 490px; }
  .para-2 { top: 581px; }
  .para-3 { top: 673px; }
  .para-4 { top: 746px; }
  .closing { top: 823px; }
  .signature { top: 866px; left: 70px; font-family: "Allura", cursive; font-size: 46px; line-height: 50px; color: #1d1d1d; }

  /* Footer decoration area */
  .footer-band {
    position: absolute;
    left: 0; bottom: 0;
    width: 857px; height: 150px;
    background: linear-gradient(180deg, var(--orange-soft) 0%, var(--orange) 100%);
  }
</style>
</head>
<body>
  <main class="letterhead">
    <header>
      <div class="brand">
        <div class="brand-name">KALESHI</div>
        <div class="brand-sub">CONSTRUCTION LTD</div>
      </div>
      <address class="contact">
        <div class="contact-title">KALESHI <span class="accent">CONSTRUCTION</span> LIMITED</div>
        <div class="contact-address">Tumbili Street, Kigamboni Shores,<br>Dar es salaam, Tanzania</div>
        <ul class="contact-list">
          <li><svg viewBox="0 0 14 14"><path fill="var(--orange)" d="M1 5c0-2 2-3 6-3s6 1 6 3l-3 1-1-2H5L4 6zM3 7h8l1 5H2z"/></svg>0754382916</li>
          <li><svg viewBox="0 0 14 14"><rect x="1" y="3" width="12" height="8" fill="var(--orange)"/><path d="M1 3l6 5 6-5" stroke="#fff" fill="none"/></svg>info@kaleshiconstruction.example</li>
          <li><svg viewBox="0 0 14 14"><circle cx="7" cy="7" r="6" fill="var(--orange)"/><path d="M4 4c2 0 2 3 4 3M9 11c0-2 2-2 2-4" stroke="#fff" fill="none"/></svg>www.kaleshiconstruction.example</li>
        </ul>
      </address>
    </header>

    <p class="letter date">Feb-03-2022</p>
    <p class="letter recipient">Mr, Peter Mallya<br>President</p>
    <p class="letter company">Mto Trading Corporation<br>123 Street Name, Suite# 10<br>City, State, 120023</p>
    <p class="letter salutation">Dear Mr, Peter</p>
    <p class="letter body-text para-1">Lorem ipsum dolor sit amet, consectetur adipisicing elit, sed do eiusmod tempor incididunt ut labore et dolore magna aliqua. Ut enim ad minim veniam, quis nostrud exercitation ullamco laboris nisi ut aliquip ex ea commodo consequat. Duis aute irure dolor in reprehenderit in voluptate velit esse cillum dolore eu fugiat nulla pariatur.</p>
    <p class="letter body-text para-2">Lorem ipsum dolor sit amet, consectetur adipisicing elit, sed do eiusmod tempor incididunt ut labore et dolore magna aliqua. Ut enim ad minim veniam, quis nostrud exercitation ullamco laboris nisi ut aliquip ex ea commodo consequat. Duis aute irure dolor in reprehenderit in voluptate velit esse cillum dolore eu fugiat nulla pariatur.</p>
    <p class="letter body-text para-3">Lorem ipsum dolor sit amet, consectetur adipisicing elit, sed do eiusmod tempor incididunt ut labore et dolore magna aliqua. Ut enim ad minim veniam, quis nostrud exercitation ullamco laboris nisi ut aliquip ex ea commodo consequat.</p>
    <p class="letter body-text para-4">Excepteur sint occaecat cupidatat non proident, sunt in culpa qui officia deserunt mollit anim id est laborum. re et dolore magnam aliquam quaerat voluptatem.</p>
    <p class="letter closing">Regards</p>
    <p class="letter signature">Daniel Mrema</p>

    <div class="footer-band" role="img" aria-label="Orange footer decoration with a charcoal accent curve"></div>
  </main>
</body>
</html>
```